依頼詳細
掲載内容詳細に関しては、別添のExcel資料を参照してください。

・デザイン参考サイト(全体の雰囲気)
https://www.korimet-hub.com/

・カラー
青系(空のイメージ)を中心にカラフルに構成してください。

・デザイン、ムード
活発でさわやかな印象にしたいです。
また地域柄かターゲット層が少し年齢高めのためフォントサイズを少し大きくしてください。

・掲載画像
提案時点では下記添付ファイル(カンプデータ)を使用してください。
当選後、本番用の画像をこちらで用意しますので、差し替えをお願いいたします。
また、雰囲気が合っていれば、指定外の画像を追加掲載いただいてOKです。

・ターゲット
BtoC
地域の個人が対象です。
特に、グランドゴルフが流行っており、中高年など若干年齢層が高めのイメージになります。

今回は、トップページデザインの募集になります。
当選の方は、希望があれば引き続き下層ページの作成及びコーディング作業を依頼可能です。
不明点、質問などありましたらメッセージ等でご連絡ください。
ページ数
1ページ
希望イメージ
シンプル 複雑
単色 カラフル
暗い 明るい
日常 高級
遊び心 厳粛
未来的 伝統的
女性的 男性的
希望する色
青系、水色系、メインカラーは青系にしてください。全体的にはカラフルにお願いします。
納品ファイル
• フォトショップ形式 (.psd)
補足説明
・資料上はサイト名(社名)や住所などは伏字にしております。ご提案時点ではそのまま作成をお願いします。当選確定後、本内容に修正をお願いいたします。
・使用画像は当選後こちらで用意します。ご提案時点では前項同様に、カンプデータ等をご使用のうえ、当選後に本内容へ差し替え修正をお願いします。
・サイズは横幅2000pxで制作をお願いします。縦に制限はありません。(コンテンツ幅は1080px内でお願いします。)
・レスポンシブデザインを想定しています。
・当選の方は、希望があれば引き続き下層ページの作成及びコーディング作業を依頼可能です。
■ 選んだ理由

どのご提案も良かったのですが、カラフルさや爽やかさの他、少しポップさ(可愛らしさ)がクライアントに好評で、mine-kaoru様を当選とさせていただきました。

■ 提案者全員のお礼・コメント

皆様ご提案ありがとうございました。
どの提案も素晴らしく、クライアントとの相談にも時間を要しました。
今後とも、宜しくお願いいたします。

```html
<!DOCTYPE html>
<html lang="ja">
<head>
<meta charset="UTF-8">
<title>スポーツ用品各種販売 トップページ</title>
<link href="https://fonts.googleapis.com/css2?family=Noto+Sans+JP:wght@400;500;700;900&family=Montserrat:wght@700;800&display=swap" rel="stylesheet">
<style>
:root{
  --blue:#1a9ad6;
  --blue-dark:#0f6fb0;
  --sky:#dff1fb;
  --sky-2:#eef8fd;
  --orange:#f39800;
  --red:#e8452c;
  --green:#3aae4a;
  --yellow:#f6c21a;
  --ink:#333;
  --muted:#777;
  --line:#d7e3ea;
  --footer:#4a4a4a;
  --white:#fff;
}
*{box-sizing:border-box;margin:0;padding:0}
html,body{width:690px;height:1200px;overflow:hidden;background:var(--white)}
body{font-family:"Noto Sans JP",sans-serif;color:var(--ink);font-size:8px;line-height:1.4}
.page{position:relative;width:690px;height:1200px;overflow:hidden}
.en{font-family:"Montserrat",sans-serif}

/* header */
.topbar{height:12px;background:#f3f3f3;font-size:5px;color:var(--muted);padding:3px 20px}
.header{position:relative;height:70px;background:var(--white)}
.logo{position:absolute;left:270px;top:8px;width:110px;height:24px;border:1px solid #bbb;display:flex;align-items:center;justify-content:center;font-weight:700;font-size:10px;color:var(--ink)}
.sns{position:absolute;left:398px;top:10px;display:flex;gap:5px}
.sns span{width:13px;height:13px;border-radius:50%;background:#9aa}
.tel{position:absolute;left:440px;top:8px;font-size:12px;font-weight:700;color:var(--blue-dark)}
.tel small{display:block;font-size:5px;font-weight:400;color:var(--muted)}
.contact-btn{position:absolute;right:18px;top:6px;width:50px;height:38px;background:var(--blue);color:#fff;font-size:6px;text-align:center;padding-top:20px}
.nav{position:absolute;left:150px;top:45px;display:flex;gap:4px}
.nav a{display:block;width:52px;height:22px;border:1px solid var(--line);font-size:7px;text-align:center;line-height:1.1;padding-top:3px;color:var(--ink);text-decoration:none}
.nav a small{display:block;font-size:4px;color:var(--muted)}
.nav a.on{background:var(--blue);color:#fff;border-color:var(--blue)}

/* hero */
.hero{position:relative;height:230px;display:grid;grid-template-columns:1.1fr 1fr 1fr;grid-template-rows:1fr 1fr;gap:2px}
.ph{display:block}
.ph-golf{grid-column:1;grid-row:1/3;background:linear-gradient(180deg,#e8e0d6 0%,#c9b9a3 45%,#8fb05a 60%,#6d9440 100%)}
.ph-ball{grid-column:2;grid-row:1;background:linear-gradient(160deg,#d8d4cc,#a8a39a)}
.ph-run{grid-column:2;grid-row:2;background:linear-gradient(180deg,#b9d3e8,#7aa84b)}
.ph-swim{grid-column:3;grid-row:1/3;background:linear-gradient(180deg,#6fc3ea,#2a8fd0 60%,#1c6fb3)}
.hero-copy{position:absolute;left:168px;top:70px}
.hero-copy h1{background:#111;color:#fff;font-size:21px;font-weight:900;padding:4px 12px;letter-spacing:1px}
.hero-copy p{display:inline-block;background:#111;color:#fff;font-size:10px;font-weight:500;padding:4px 10px;margin-top:3px;line-height:1.6}
.badge{position:absolute;left:112px;top:22px;width:66px;height:66px;border-radius:50%;background:var(--red);color:#fff;font-weight:900;font-size:10px;text-align:center;padding-top:14px;line-height:1.3;border:3px solid var(--yellow)}

/* news */
.news{position:relative;height:115px}
.sec-title{color:var(--blue);font-size:22px;font-weight:800;letter-spacing:1px;line-height:1.2}
.news .sec-title{position:absolute;left:156px;top:36px}
.news-list{position:absolute;left:250px;top:26px;width:280px;height:80px;border-right:4px solid var(--line);overflow:hidden}
.news-item{padding:2px 0 3px;border-bottom:1px solid var(--line)}
.news-item time{display:block;font-size:5px;color:var(--muted)}
.news-item p{font-size:5.5px;white-space:nowrap;overflow:hidden}

/* federation bar */
.fed{height:46px;background:var(--sky);display:flex;align-items:center;padding:0 160px;gap:8px}
.fed-mark{width:18px;height:18px;border:2px solid var(--blue);border-radius:3px}
.fed h2{font-size:15px;font-weight:900;color:var(--blue-dark);flex:1}
.fed a{width:62px;height:28px;background:var(--blue);color:#fff;font-size:5.5px;text-align:center;padding-top:8px;text-decoration:none}

/* topics */
.topics{position:relative;height:170px}
.topics .sec-title{position:absolute;left:156px;top:12px}
.tabs{position:absolute;left:300px;top:16px;display:flex;gap:2px}
.tabs span{display:block;width:42px;height:14px;font-size:5.5px;text-align:center;line-height:14px;color:#fff}
.tabs .all{background:#fff;color:var(--blue);border:1px solid var(--blue);line-height:12px}
.t-blue{background:var(--blue)}.t-orange{background:var(--orange)}.t-green{background:var(--green)}.t-red{background:var(--red)}.t-yellow{background:var(--yellow)}
.topic-list{position:absolute;left:300px;top:40px;width:230px}
.topic-row{display:flex;align-items:center;gap:6px;height:20px;border-bottom:1px solid var(--line);font-size:5.5px}
.topic-row time{color:var(--muted);width:32px}
.topic-row .tag{width:30px;height:9px;font-size:4.5px;color:#fff;text-align:center;line-height:9px}
.topic-row .new{background:var(--red);color:#fff;font-size:4px;padding:0 3px;margin-left:2px}
.more{position:absolute;left:386px;top:150px;width:58px;height:12px;border:1px solid var(--line);font-size:5px;text-align:center;line-height:11px;color:var(--muted)}

/* promos */
.promos{height:190px;display:flex;gap:8px;justify-content:center;padding-top:6px}
.card{width:122px;height:176px;position:relative;color:#fff}
.card-video{background:linear-gradient(180deg,#9c3b32,#5a6f8e 60%,#2e3b52)}
.play{position:absolute;left:48px;top:74px;width:26px;height:26px;border-radius:50%;background:rgba(255,255,255,.85)}
.card-order{background:var(--orange);padding:24px 10px}
.card-maker{background:var(--blue);padding:24px 10px}
.card h3{font-size:10px;font-weight:900;line-height:1.4;text-align:center}
.card p{font-size:5px;margin-top:8px;line-height:1.6}
.card .photo{display:block;width:100%;height:52px;margin-top:10px}
.card-order .photo{background:linear-gradient(135deg,#f7c97a,#e07d1e)}
.card-maker .photo{background:linear-gradient(135deg,#8bd0f2,#2d78b8)}

/* access */
.access{position:relative;height:215px;background:var(--sky-2)}
.access .sec-title{position:absolute;left:160px;top:14px}
.access-logo{position:absolute;left:160px;top:46px;width:78px;height:18px;border:1px solid #bbb;background:#fff;font-size:8px;font-weight:700;text-align:center;line-height:16px}
.addr{position:absolute;left:160px;top:72px;font-size:5.5px;line-height:1.7}
.addr strong{display:block;font-size:9px;color:var(--ink);line-height:1.4}
.map{position:absolute;left:340px;top:40px;width:190px;height:110px;background:linear-gradient(140deg,#e9efe3,#cfe0c4 60%,#b9d4e6)}
.btn{position:absolute;top:166px;height:24px;background:var(--blue);color:#fff;font-size:6px;display:flex;align-items:center;justify-content:center;gap:5px}
.btn-contact{left:160px;width:90px}
.btn-park{left:340px;width:190px}

/* footer */
.footer{height:152px;background:var(--footer);color:#fff;padding-top:12px}
.foot-nav{display:flex;justify-content:center;gap:14px;font-size:5.5px;color:#ddd}
.foot-logo{width:78px;height:18px;margin:22px auto 0;background:#fff;color:var(--ink);font-weight:700;font-size:8px;text-align:center;line-height:18px}
.copy{text-align:center;font-size:5px;color:#bbb;margin-top:10px}
</style>
</head>
<body>
<div class="page">
  <div class="topbar">京都府 ─ スポーツ用品専門店</div>
  <header class="header">
    <div class="logo">会社logo</div>
    <div class="sns"><span></span><span></span></div>
    <div class="tel">
      <svg width="9" height="9" viewBox="0 0 24 24"><path fill="#0f6fb0" d="M6.6 10.8a15 15 0 006.6 6.6l2.2-2.2a1 1 0 011-.25 11 11 0 003.6.6 1 1 0 011 1V20a1 1 0 01-1 1A17 17 0 013 4a1 1 0 011-1h3.5a1 1 0 011 1c0 1.2.2 2.4.6 3.6a1 1 0 01-.25 1z"/></svg>
      0123-45-6789<small>営業時間 10:00〜19:00 定休日 火曜日</small>
    </div>
    <div class="contact-btn">お問い合わせ</div>
    <nav class="nav">
      <a class="on" href="#">ホーム<small>Home</small></a>
      <a href="#">店舗案内<small>Shop</small></a>
      <a href="#">取扱商品<small>Item</small></a>
      <a href="#">オーダー<small>Order</small></a>
      <a href="#">ブログ<small>Blog</small></a>
      <a href="#">連盟支部<small>League</small></a>
    </nav>
  </header>

  <section class="hero">
    <div class="ph ph-golf" role="img" aria-label="グラウンドゴルフのクラブとボールの写真"></div>
    <div class="ph ph-ball" role="img" aria-label="野球ボールとグラブの写真"></div>
    <div class="ph ph-run" role="img" aria-label="グラウンドでサッカーをする写真"></div>
    <div class="ph ph-swim" role="img" aria-label="プールで泳ぐ競泳の写真"></div>
    <div class="badge">取扱い<br>メーカー<br>多数</div>
    <div class="hero-copy">
      <h1>スポーツ用品各種販売</h1>
      <p>お取り寄せも可能です。<br>是非、お気軽にご来店ください。</p>
    </div>
  </section>

  <section class="news">
    <h2 class="sec-title en">NEWS</h2>
    <div class="news-list">
      <div class="news-item"><time>2021.02.15</time><p>新商品のグラウンドゴルフ用品が入荷しました。ぜひ店頭でご覧ください。</p></div>
      <div class="news-item"><time>2021.02.10</time><p>営業時間変更のお知らせ。当面の間、平日は18時までの営業となります。</p></div>
      <div class="news-item"><time>2021.02.01</time><p>春のチームユニフォーム注文受付を開始しました。お早めにどうぞ。</p></div>
      <div class="news-item"><time>2021.01.25</time><p>定休日のお知らせ。今月の臨時休業日を掲載しています。</p></div>
    </div>
  </section>

  <section class="fed">
    <span class="fed-mark"></span>
    <h2>緑丘軟式野球連盟 〇〇支部</h2>
    <a href="#">支部情報は<br>こちら</a>
  </section>

  <section class="topics">
    <h2 class="sec-title en">TOPICS</h2>
    <div class="tabs">
      <span class="all">ALL</span><span class="t-blue">新着情報</span><span class="t-orange">軟式野球</span><span class="t-green">商品案内</span><span class="t-red">イベント</span>
    </div>
    <div class="topic-list">
      <div class="topic-row"><time>2021.02.15</time><span class="tag t-blue">新着情報</span>新作アイテムのご紹介<span class="new">NEW</span></div>
      <div class="topic-row"><time>2021.02.12</time><span class="tag t-orange">軟式野球</span>支部大会の結果報告</div>
      <div class="topic-row"><time>2021.02.08</time><span class="tag t-green">商品案内</span>春の新作シューズ</div>
      <div class="topic-row"><time>2021.02.03</time><span class="tag t-red">イベント</span>体験会のお知らせ</div>
      <div class="topic-row"><time>2021.01.28</time><span class="tag t-blue">新着情報</span>年間予定を更新しました</div>
    </div>
    <div class="more">一覧を見る</div>
  </section>

  <section class="promos">
    <div class="card card-video" role="img" aria-label="店舗紹介動画のサムネイル写真">
      <span class="play"></span>
    </div>
    <div class="card card-order">
      <h3>オリジナルオーダー<br>制作できます!</h3>
      <p>ユニフォームやバッグなど、チームに合わせた名入れやオーダー製作を承ります。</p>
      <span class="photo" role="img" aria-label="オーダーユニフォームの写真"></span>
    </div>
    <div class="card card-maker">
      <h3>取扱いメーカー多数!<br>ご購入相談承ります!</h3>
      <p>各種メーカー商品を取り揃えております。お探しの品はお気軽にご相談ください。</p>
      <span class="photo" role="img" aria-label="スポーツ用品売り場の写真"></span>
    </div>
  </section>

  <section class="access">
    <h2 class="sec-title en">ACCESS</h2>
    <div class="access-logo">会社logo</div>
    <div class="addr">
      京都府〇〇市〇〇町1-2-3<br>
      〒123-4567 最寄駅より徒歩5分<br>
      営業時間 10:00〜19:00 定休日 火曜日
      <strong>TEL. 0123-45-6789<br>FAX. 0987-65-4321</strong>
    </div>
    <div class="map" role="img" aria-label="店舗周辺の地図"></div>
    <div class="btn btn-contact">
      <svg width="8" height="8" viewBox="0 0 24 24"><path fill="#fff" d="M2 5h20v14H2zM4 7l8 6 8-6"/></svg>お問い合わせ</div>
    <div class="btn btn-park">
      <svg width="8" height="8" viewBox="0 0 24 24"><path fill="#fff" d="M12 2a7 7 0 00-7 7c0 5 7 13 7 13s7-8 7-13a7 7 0 00-7-7zm0 9.5A2.5 2.5 0 1112 6a2.5 2.5 0 010 5.5z"/></svg>駐車場の案内はこちらをご覧ください</div>
  </section>

  <footer class="footer">
    <nav class="foot-nav"><span>ホーム</span><span>店舗案内</span><span>取扱商品</span><span>オーダー</span><span>ブログ</span><span>連盟支部</span><span>お問い合わせ</span></nav>
    <div class="foot-logo">会社logo</div>
    <p class="copy">© 2021 会社logo All Rights Reserved.</p>
  </footer>
</div>
</body>
</html>
```